1 Page Bio, describing our Mission to buy multifamily properties in Colorado Springs.

I am uploading a sample of an associate who is doing a similar thing in Tampa Florida. I will also upload an attempt by my assistant to make the flyer and I will upload 3 pictures to use, along with another document that has text to add. I want to be able to edit the document pretty easily inside a google doc. thanks, I want it to look clean and professional.

```html
<!DOCTYPE html>
<html lang="en">
<head>
<meta charset="utf-8">
<title>Wade &amp; Glen Kessler – One Page Bio</title>
<link rel="stylesheet" href="https://fonts.googleapis.com/css2?family=Source+Sans+3:wght@400;600;700&display=swap">
<style>
  :root {
    --backdrop: #b3b3b3;
    --paper: #ffffff;
    --navy: #1b3368;
    --gold: #dcc57f;
    --gold-pale: #fbf8f1;
    --maroon: #653232;
    --rule: #8a5a5a;
    --ink: #3a3a3a;
    --ink-dark: #2b2b2b;
    --accent-blue: #1d2f6e;
  }
  * { box-sizing: border-box; margin: 0; padding: 0; }
  html, body { width: 1200px; height: 1200px; overflow: hidden; }
  body {
    background: var(--backdrop);
    font-family: "Source Sans 3", "Source Sans Pro", sans-serif;
    color: var(--ink);
    position: relative;
  }
  .page {
    position: absolute; left: 197px; top: 79px;
    width: 806px; height: 1042px;
    background: var(--paper);
  }
  .masthead {
    position: absolute; left: 37px; top: 0; width: 731px; height: 161px;
    background: var(--navy); overflow: hidden;
  }
  .masthead .skyline {
    position: absolute; left: 237px; top: 0; width: 494px; height: 161px;
    background: linear-gradient(180deg, rgba(44,79,163,0.35), rgba(30,60,150,0.85));
  }
  .brand {
    position: absolute; left: 24px; top: 44px;
    color: var(--gold); font-weight: 700;
    font-size: 44px; line-height: 40px; letter-spacing: 1px;
  }
  .mission-rule { position: absolute; left: 0; width: 806px; height: 1px; background: var(--rule); }
  .mission {
    position: absolute; left: 37px; top: 162px; width: 731px; height: 37px;
    background: var(--gold); color: var(--accent-blue);
    font-weight: 700; font-size: 14.5px; line-height: 37px; padding-left: 23px;
    white-space: nowrap;
  }
  .mission strong { font-size: 19px; }
  .mission-bar { position: absolute; left: 37px; top: 199px; width: 731px; height: 18px; background: var(--navy); }

  .sidebar {
    position: absolute; left: 37px; top: 217px; width: 249px; height: 687px;
    background: linear-gradient(180deg, var(--gold-pale) 0%, #f1e6c6 45%, var(--gold) 100%);
  }
  .side-section { position: absolute; left: 0; width: 249px; }
  .side-title {
    border-top: 1px solid var(--rule); border-bottom: 1px solid var(--rule);
    height: 35px; line-height: 34px; padding-left: 17px;
    color: var(--maroon); font-weight: 700; font-size: 19px;
  }
  .side-text { padding: 8px 17px 0; font-size: 15px; line-height: 20px; }
  .side-text ul { list-style: none; }
  .side-text li { position: relative; padding-left: 14px; }
  .side-text li::before { content: "•"; position: absolute; left: 1px; }

  .contact {
    position: absolute; left: 37px; top: 904px; width: 249px; height: 116px;
    background: var(--maroon); color: #fff;
    padding: 22px 0 0 59px; font-size: 15px; line-height: 20px;
  }
  .contact .label { font-weight: 700; }
  .contact .line { position: relative; font-weight: 700; }
  .contact svg { position: absolute; left: -27px; top: 4px; }
  .base-bar { position: absolute; left: 37px; top: 1020px; width: 731px; height: 22px; background: var(--navy); }

  .team { position: absolute; left: 318px; top: 231px; width: 450px; }
  .team h2 { color: var(--maroon); font-size: 19px; font-weight: 700; height: 35px; line-height: 30px; border-bottom: 1px solid var(--rule); width: 330px; }
  .team h3 { color: var(--accent-blue); font-size: 18px; font-weight: 700; height: 35px; line-height: 34px; border-bottom: 1px solid var(--rule); width: 330px; }
  .person-name { font-weight: 700; color: var(--ink-dark); font-size: 15px; line-height: 20px; margin-top: 10px; }
  .person-name.spaced { margin-top: 20px; }
  .team ul { list-style: none; font-size: 15px; line-height: 20px; }
  .team li { position: relative; padding-left: 21px; }
  .team li::before { content: ""; position: absolute; left: 2px; top: 8px; width: 5px; height: 5px; border-radius: 50%; background: var(--maroon); }
  .advisors-head { margin-top: 14px; border-top: 1px solid var(--rule); width: 330px; }
  .beside-photo { padding-right: 130px; }

  .portrait { position: absolute; border-radius: 50%; }
  .portrait.pair { left: 644px; top: 226px; width: 120px; height: 118px; background: radial-gradient(circle at 50% 45%, #7a7466, #4a4a3e); }
  .portrait.advisor { width: 112px; height: 112px; background: radial-gradient(circle at 50% 45%, #d8d8d8, #9a9a9a); }
  .portrait.one { left: 654px; top: 585px; }
  .portrait.two { left: 663px; top: 759px; width: 86px; height: 110px; }
</style>
</head>
<body>
<div class="page">
  <header class="masthead">
    <div class="skyline" role="img" aria-label="Blue city skyline silhouette illustration"></div>
    <div class="brand">WADE &amp;<br>GLEN KESSLER</div>
  </header>

  <div class="mission-rule" style="top:161px"></div>
  <div class="mission"><strong>THE MISSION</strong> : To create a family business by purchasing Multifamily Residences, one at a time.</div>
  <div class="mission-rule" style="top:199px"></div>
  <div class="mission-bar"></div>

  <aside class="sidebar">
    <section class="side-section" style="top:49px">
      <div class="side-title">VALUES</div>
      <div class="side-text">To provide a white glove experience to all residences with a clean, safe, and fun environment.</div>
    </section>
    <section class="side-section" style="top:204px">
      <div class="side-title">THE PROCESS</div>
      <div class="side-text">Buy right, manage right, and finance right.</div>
    </section>
    <section class="side-section" style="top:316px">
      <div class="side-title">THE MARKET</div>
      <div class="side-text">Colorado Springs
        <ul>
          <li>Projected job growth of nearly 50%</li>
          <li>Below average unemployment rates.</li>
          <li>Above-average incomes.</li>
          <li>Solid economy, military, aerospace, electronics industry, and tourism.</li>
        </ul>
      </div>
    </section>
    <section class="side-section" style="top:564px">
      <div class="side-title">THE TARGET</div>
      <div class="side-text">B and C class assets located in Colorado Springs or nearby submarkets.</div>
    </section>
  </aside>

  <div class="contact">
    <div class="label">Contact:</div>
    <div>Wade &amp; Glen Kessler</div>
    <div class="line">
      <svg width="12" height="12" viewBox="0 0 12 12"><circle cx="6" cy="6" r="6" fill="#fff"/><path d="M3.6 3.2l1.2-.4.8 1.5-.7.6c.3.7.9 1.3 1.6 1.6l.6-.7 1.5.8-.4 1.2C6.5 8 4 5.5 3.6 3.2z" fill="#653232"/></svg>
      719-555-0148</div>
    <div class="line">
      <svg width="12" height="12" viewBox="0 0 12 12"><circle cx="6" cy="6" r="6" fill="#fff"/><path d="M3 6.2l6-3-2 6-1.2-2z" fill="#653232"/></svg>
      wkessler@example.com</div>
  </div>

  <main class="team">
    <h2>THE TEAM</h2>
    <h3>Principals</h3>
    <div class="person-name">Wade Kessler</div>
    <ul>
      <li>Licensed Colorado Real Estate Agent 18 years.</li>
      <li>Broker-Owner of two HomeCrest Franchises 7 and 2 Years.</li>
      <li>Real Estate investing for 5 years.</li>
      <li>Member of Keystone Investors Academy.</li>
      <li>Married 24 years to Laura, parenting 10 children together.</li>
      <li>Appeared on Sam and Leo’s Apartment Hour podcast Episode 43</li>
      <li>$2M portfolio.</li>
    </ul>
    <div class="person-name spaced">Glen Kessler</div>
    <ul style="line-height:22px">
      <li>Retired Electrical Engineer.</li>
      <li>Active Real Estate Investor/Consultant.</li>
      <li>Net worth over $4M</li>
      <li>15 Grandchildren.</li>
    </ul>
    <h3 class="advisors-head">Advisors</h3>
    <div class="person-name">Dean Harlow</div>
    <ul>
      <li>General partner on 103 Apartments</li>
      <li>Acquiring 101 more apartments in Q1 - 2020</li>
      <li>Flips 4-8 houses a year</li>
      <li>Active member in the Sam &amp; Leo Community</li>
      <li>Accountability coach</li>
    </ul>
    <div class="person-name">Brent Hale</div>
    <ul>
      <li class="beside-photo">Brent is the owner/operator of Summit Residential Group and Summit Residential Management</li>
      <li>He has been in the real estate business for 13 years<br>and has created a portfolio of over 1000 units while growing Summit Management with team of 15 staff members.</li>
      <li>He has taught real estate for the past 6 years and has dozens of highly successful students. Brent uses his extensive real estate experience to teach his students the “real” side of real estate.</li>
    </ul>
  </main>

  <div class="portrait pair" role="img" aria-label="Photo of the two principals standing together outdoors"></div>
  <div class="portrait advisor one" role="img" aria-label="Black and white headshot of advisor Dean Harlow"></div>
  <div class="portrait advisor two" role="img" aria-label="Black and white headshot of advisor Brent Hale"></div>

  <div class="base-bar"></div>
</div>
</body>
</html>
```